The Perfect Business Card for PineHarbor

I am looking for a business card which beautifully incorporates my logo, reflects my business and looks special, elegant and clean.

```html
<!DOCTYPE html>
<html lang="en">
<head>
<meta charset="utf-8">
<title>PineHarbor Business Card</title>
<link href="https://fonts.googleapis.com/css2?family=Marcellus&family=Roboto:wght@300;400&display=swap" rel="stylesheet">
<style>
  :root {
    --page: #f6f6f6;
    --card-white: #ffffff;
    --green-dark: #4c6330;
    --green-mid: #5f7a3a;
    --green-light: #7b9a4b;
    --rule: #7d8f5a;
    --ink-light: #ffffff;
    --shadow: rgba(0, 0, 0, 0.18);
  }
  html, body {
    margin: 0;
    padding: 0;
    width: 800px;
    height: 1200px;
    overflow: hidden;
    background: var(--page);
  }
  .canvas {
    position: relative;
    width: 800px;
    height: 1200px;
  }
  .card {
    position: absolute;
    left: 100px;
    width: 600px;
    height: 343px;
    box-shadow: 0 4px 14px var(--shadow);
    overflow: hidden;
  }
  .card--front {
    top: 200px;
    background: var(--card-white);
  }
  .card--back {
    top: 660px;
    background: linear-gradient(90deg, var(--green-light) 0%, var(--green-mid) 55%, var(--green-dark) 100%);
  }
  .brand {
    position: absolute;
    display: flex;
    align-items: center;
    gap: 12px;
    font-family: "Marcellus", serif;
    white-space: nowrap;
  }
  .brand__dot {
    border-radius: 50%;
    flex: none;
  }
  .card--front .brand {
    left: 52px;
    top: 150px;
    font-size: 30px;
    color: var(--green-mid);
  }
  .card--front .brand__dot {
    width: 14px;
    height: 14px;
    background: var(--green-mid);
  }
  .card--back .brand {
    left: 150px;
    top: 148px;
    font-size: 42px;
    color: var(--ink-light);
  }
  .card--back .brand__dot {
    width: 14px;
    height: 14px;
    background: var(--ink-light);
  }
  .divider {
    position: absolute;
    left: 301px;
    top: 78px;
    width: 1.5px;
    height: 190px;
    background: var(--rule);
  }
  .contact-block {
    position: absolute;
    left: 316px;
    top: 92px;
    color: var(--green-mid);
  }
  .person__name {
    font-family: "Marcellus", serif;
    font-size: 26px;
    line-height: 1;
    margin: 0;
    color: var(--green-dark);
    letter-spacing: 0.3px;
  }
  .person__title {
    font-family: "Roboto", sans-serif;
    font-weight: 300;
    font-size: 16px;
    margin: 3px 0 0;
  }
  .contact-list {
    list-style: none;
    margin: 18px 0 0;
    padding: 0;
    font-family: "Roboto", sans-serif;
    font-weight: 300;
    font-size: 16px;
    line-height: 1.1;
  }
  .contact-list__item {
    display: flex;
    align-items: flex-start;
    gap: 8px;
    margin-bottom: 10px;
  }
  .contact-list__icon {
    width: 12px;
    height: 12px;
    flex: none;
    margin-top: 3px;
    fill: var(--green-mid);
  }
</style>
</head>
<body>
<main class="canvas">

  <section class="card card--front" aria-label="Business card front">
    <div class="brand">
      <span class="brand__dot"></span>
      <span class="brand__name">PineHarbor</span>
    </div>
    <div class="divider"></div>
    <div class="contact-block">
      <h1 class="person__name">YOUR NAME HERE</h1>
      <p class="person__title">Your Title Here</p>
      <ul class="contact-list">
        <li class="contact-list__item">
          <svg class="contact-list__icon" viewBox="0 0 12 12" aria-hidden="true"><path d="M2.5 0.8 L4.3 0.5 L5 3.4 L3.8 4.3 Q4.6 6.6 6.6 8 L7.6 6.9 L10.5 7.7 L10.2 9.6 Q9.6 11.2 7.6 10.8 Q2 9 0.9 3.2 Q0.8 1.3 2.5 0.8 Z"/></svg>
          <span>123-456-7890</span>
        </li>
        <li class="contact-list__item">
          <svg class="contact-list__icon" viewBox="0 0 12 12" aria-hidden="true"><path d="M6 0.5 A4 4 0 0 1 10 4.5 Q10 7 6 11.5 Q2 7 2 4.5 A4 4 0 0 1 6 0.5 Z M6 3 A1.5 1.5 0 1 0 6 6 A1.5 1.5 0 1 0 6 3 Z" fill-rule="evenodd"/></svg>
          <span>123 NW Somewhere St.<br>Somewhere City, 1111</span>
        </li>
        <li class="contact-list__item">
          <svg class="contact-list__icon" viewBox="0 0 12 12" aria-hidden="true"><path d="M0.5 2.5 H11.5 V10 H0.5 Z M1 3 L6 6.8 L11 3" stroke="#ffffff" stroke-width="0.8"/></svg>
          <span>your@email.com</span>
        </li>
      </ul>
    </div>
  </section>

  <section class="card card--back" aria-label="Business card back">
    <div class="brand">
      <span class="brand__dot"></span>
      <span class="brand__name">PineHarbor</span>
    </div>
  </section>

</main>
</body>
</html>
```